Granite Ridge College-Pinecrest Welcome Week

I am the Student Activities Coordinator at Granite Ridge College-Pinecrest. For Welcome Week 2013, I need a standard poster 24x36 with the list of events happening. Our theme is based on the popular Friday Late Laughs video "We Got a Kite"
http://www.vidtrove.example/clip/Q4mZp8sLwTe
Our theme is:
We're at the 'Crest!
Welcome Week 2013
Graphics on the poster should reflect popular images/designs of FLL We Got a Kite. However, the boat should be a steamboat instead of the yacht image.
Unfortunately, I have a lot of text to fit on the poster. Traditionally we go with 3 margins listing events. I'm attaching the word document of events and our logo to this proposal. I'll also attach a few google images of "We Got a Kite" that align with the type of theme I'm looking for.
One last thing, our logo contains mountains listing all of the different campuses. Remove the campus names and mountains all together. Use simply the Colorado flag C and "Granite Ridge College".
Thanks for considering this brief!
Glen
Target Market(s)
Our college students love to ski and snowboard. In fact, one of our degrees is "Alpine Slope Commerce". Their ages are 18-22.
Industry/Entity Type
Events
Look and feel

```html
<!DOCTYPE html>
<html lang="en">
<head>
<meta charset="utf-8">
<title>We're at the 'Crest! – Welcome Week 2013</title>
<link rel="stylesheet" href="https://fonts.googleapis.com/css2?family=Arimo:wght@400;700&family=Lobster&family=Questrial&display=swap">
<style>
  :root {
    --sky-top: #2a5fa8;
    --sky-mid: #6f9fd2;
    --water-top: #3f8fcf;
    --water-deep: #0f4f8c;
    --water-bottom: #0b3c72;
    --title-red: #e23a36;
    --title-yellow: #f7e43a;
    --heading-yellow: #ffe53d;
    --heading-shadow: #1a2a6e;
    --text-white: #ffffff;
    --contact-gold: #f0d45a;
    --logo-red: #d8322f;
  }
  * { margin: 0; padding: 0; box-sizing: border-box; }
  html, body { width: 800px; height: 1200px; overflow: hidden; }
  body { font-family: "Arimo", Arial, sans-serif; color: var(--text-white); }

  .poster { position: relative; width: 800px; height: 1200px; overflow: hidden; }

  .scene-photo {
    position: absolute; inset: 0;
    background: linear-gradient(180deg,
      var(--sky-top) 0%, var(--sky-mid) 22%, #9cc3e6 30%,
      var(--water-top) 36%, var(--water-deep) 60%, var(--water-bottom) 100%);
  }

  .title-badge { position: absolute; left: 92px; top: 56px; width: 600px; height: 112px; }
  .title {
    position: absolute; left: 92px; top: 62px; width: 600px;
    text-align: center; font-family: "Lobster", cursive;
    font-size: 62px; line-height: 96px; color: var(--title-yellow);
    text-shadow: 2px 3px 0 #8a1413;
  }
  .subtitle {
    position: absolute; left: 0; top: 180px; width: 800px; text-align: center;
    font-family: "Questrial", sans-serif; font-size: 34px; color: var(--text-white);
  }

  .day { position: absolute; width: 180px; }
  .day h2 {
    font-family: "Lobster", cursive; font-weight: 400; font-size: 21px;
    color: var(--heading-yellow); text-shadow: 1px 2px 2px var(--heading-shadow);
    margin-bottom: 7px; white-space: nowrap;
  }
  .events { list-style: none; }
  .event { font-size: 13px; line-height: 15.5px; margin-bottom: 5px; }
  .note { font-size: 13px; line-height: 15.5px; margin-top: 18px; }

  .brand-mark {
    position: absolute; display: flex; align-items: center; gap: 14px;
  }
  .brand-mark .dot { border-radius: 50%; background: var(--logo-red); flex: none; }
  .brand-mark .name {
    font-family: "Arimo", Arial, sans-serif; font-weight: 700;
    color: var(--text-white); text-transform: uppercase; white-space: nowrap;
  }
  .brand-center { left: 262px; top: 728px; }
  .brand-center .dot { width: 104px; height: 104px; }
  .brand-center .name { font-size: 28px; line-height: 32px; }

  .contact { position: absolute; right: 28px; top: 1044px; text-align: right; }
  .contact .more { font-weight: 700; font-size: 13px; color: var(--contact-gold); margin-bottom: 8px; }
  .contact .brand-mark { position: static; justify-content: flex-end; gap: 6px; margin-bottom: 8px; }
  .contact .brand-mark .dot { width: 30px; height: 30px; }
  .contact .brand-mark .name { font-size: 13px; line-height: 15px; text-align: left; }
  .contact address { font-style: normal; font-size: 11px; line-height: 14px; color: var(--contact-gold); }
</style>
</head>
<body>
<main class="poster">
  <div class="scene-photo" role="img" aria-label="Photo of a white boat gliding on calm blue water in front of snowy mountains under a cloudy blue sky"></div>

  <svg class="title-badge" viewBox="0 0 600 112" aria-hidden="true">
    <path d="M30 18 Q300 0 575 10 Q598 14 592 40 L584 84 Q580 104 556 102 Q300 114 34 104 Q8 102 10 78 L14 36 Q16 20 30 18 Z" fill="var(--title-red)"/>
  </svg>
  <h1 class="title">We're at the 'Crest!</h1>
  <p class="subtitle">Welcome Week 2013</p>

  <section class="day" style="left:28px;top:444px;">
    <h2>Thursday August 22</h2>
    <ul class="events">
      <li class="event">Residence Hall Move-In<br>12:00pm-3:00pm<br>Ridge Hall</li>
      <li class="event">Brunch<br>10:00am-1:00pm<br>Dining Hall</li>
      <li class="event">International Students<br>Orientation<br>3:00pm<br>Boulder 121</li>
      <li class="event">Dinner<br>5:00pm-6:30pm<br>Dining Hall</li>
      <li class="event">Hot Springs Waterslide Party<br>7:00pm-9:00pm<br>Old Mill Hot Springs</li>
    </ul>
  </section>

  <section class="day" style="left:28px;top:766px;">
    <h2>Friday August 23</h2>
    <ul class="events">
      <li class="event">Breakfast<br>7:30am-9:00am<br>Dining Hall</li>
      <li class="event">Hike Trout Creek Falls<br>9:00am-11:30am<br>Shuttle leaves Ridge Hall at<br>8:30am</li>
      <li class="event">BBQ and Faculty Ice Cream<br>Social<br>12:00pm-1:30pm<br>Dining Hall</li>
      <li class="event">Kick Off Party: Inflatables<br>1:30pm-4:00pm<br>Upper Parking Lot</li>
      <li class="event">Dinner<br>5:00pm-6:00pm<br>Dining Hall</li>
      <li class="event">Free Concert<br>7:00pm<br>Pinecrest Resort Base<br>(PTS Buses to Resort,<br>5:35pm Last Bus)</li>
    </ul>
  </section>

  <section class="day" style="left:218px;top:478px;">
    <h2>Saturday August 24</h2>
    <ul class="events">
      <li class="event">Main Street Farmers Market<br>9:00am-2:00pm<br>6th &amp; Aspen (walking dist.)</li>
      <li class="event">Brunch<br>10:00am-1:00pm<br>Dining Hall</li>
      <li class="event">Cedar Park Hot Springs<br>2:00pm-5:00pm<br>Shuttle leaves Ridge Hall at<br>1:30pm</li>
    </ul>
  </section>

  <section class="day" style="left:413px;top:514px;">
    <ul class="events">
      <li class="event">Dinner<br>5:00-6:00pm<br>Dining Hall</li>
      <li class="event">Free Movie on the Mountain:<br>Starfall Trials<br>8:00pm<br>(PTS Buses to Resort,<br>5:35pm Last Bus)</li>
    </ul>
  </section>

  <section class="day" style="left:603px;top:505px;">
    <h2>Sunday August 25</h2>
    <ul class="events">
      <li class="event">Brunch<br>10:00am-1:00pm<br>Dining Hall</li>
      <li class="event">Alpine Slide/Volleyball<br>2:00pm-4:00pm<br>Meet at Hollis Hill</li>
      <li class="event">Dinner<br>5:00pm-6:00pm<br>Dining Hall</li>
      <li class="event">Mandatory All Hall Meeting<br>6:00pm<br>Auditorium</li>
      <li class="event">RHA Super Sunday Program<br>8:00pm<br>Ridge Hall: MPR</li>
    </ul>
  </section>

  <section class="day" style="left:603px;top:814px;">
    <h2>Friday August 30</h2>
    <ul class="events">
      <li class="event">Late Night Climbing<br>9:00pm<br>Gym</li>
    </ul>
    <p class="note">ALL EVENTS ARE FREE<br>UNLESS OTHERWISE<br>NOTED</p>
  </section>

  <div class="brand-mark brand-center">
    <span class="dot"></span>
    <span class="name">Granite<br>Ridge<br>College</span>
  </div>

  <section class="day" style="left:218px;top:893px;">
    <h2>Monday August 26</h2>
    <ul class="events">
      <li class="event">Regular Dining Hall Hours<br>Begin</li>
      <li class="event">“Being Alone Sucks!”<br>9:00pm<br>Auditorium</li>
    </ul>
  </section>

  <section class="day" style="left:405px;top:893px;">
    <h2>Wednesday August 28</h2>
    <ul class="events">
      <li class="event">Free Bowling<br>9:00pm<br>Frost Lanes</li>
    </ul>
  </section>

  <section class="day" style="left:218px;top:1036px;">
    <h2>Tuesday August 27</h2>
    <ul class="events">
      <li class="event">Newly Roommate Game<br>7:00pm-8:00pm<br>Ridge Hall: MPR</li>
      <li class="event">Free Gelato<br>8:00pm-9:00pm<br>Pinecone Gelato 7th and Birch</li>
    </ul>
  </section>

  <section class="day" style="left:405px;top:1036px;">
    <h2>Thursday August 29</h2>
    <ul class="events">
      <li class="event">Club Fair<br>10:00am-2:00pm<br>Dining Hall</li>
      <li class="event" style="margin-top:14px;">Black Light Dodgeball<br>9:00pm<br>Gym</li>
    </ul>
  </section>

  <aside class="contact">
    <p class="more">For more details</p>
    <div class="brand-mark">
      <span class="dot"></span>
      <span class="name">Granite Ridge<br>College</span>
    </div>
    <address>
      Granite Ridge College<br>
      PO Box 4821, Pinecrest,<br>
      CO 80477-4821 USA<br>
      +1-555-014-2270<br>
      info@graniteridge.example
    </address>
  </aside>
</main>
</body>
</html>
```